Colourful Bold Design for Pet Insurance Website

PLEASE NOTE THAT THIS PROJECT HAS BEEN EXTENDED. Please read the PROJECT EXTENSION DOCUMENT BEFORE STARTING WORK ON ANY DESIGNS.

We are looking for a colourful bold new template design for our JOOMLA HOMEPAGE and a matching design for our new WORDPRESS BLOG.

The website will help pet owners work out which insurance policy best meets their needs. The aim of the website is to explain policy differences in a plain clear manner.

The website will need to have a professional colourful image. It needs to be BOLD, CLEAN AND SHARP rather than soft, pastel and cuddly.

COLOUR SCHEME
The website needs to have a bold colourful design on a white background.
On the inner pages we will have five different types of policies which will be colour coded. We would ideally therefore like to incorporate five distinct colours in the design. See attached document for example of colour schemes we like.

LOGO
We want to keep the existing logo. Please find the file attached. You may though change the logo colours.

CONTENT
One of the reasons for the new design is that we want to change the style of the homepage and include new content. Our current homepage can be found at www.cover-compare-quizzo.co.uk.

Content Required
Slideshow
Article Intro.. About Pet Insurance
Policy Lookup Box (see existing site… you can change the design of this)
Six link options (see links on left of current page)
Latest Reviews (List of 6)
Ad (Same dimensions as currently on homepage)

News and Comment Section - To include Three or Four Articles, Title, Intro to article (probably 3 or 4 lines .. about 400px wide), Read more link
Social Media Section
Friendwall Plugin with Feed
Latest Tweets Plugin
Pet Charities Latest Tweets
Footer
Larger footer with lots of links grouped in sections

It does not need to include the clipart pic of the pets which is on the current homepage.

Examples of Websites and Templates We Like
http://www.brindlevox.com/ (like colours… fonts…layout)
http://layoutdemo.quarnofield.com/?template=elated&path=/... (like the clarity, "white" space etc)
http://www.skellpravo.com/demo/58817.html (like white space, clear easy to read fonts… don’t like colour scheme, size of top picture)
http://www.skellpravo.com/website-templates/62391.html (like colour scheme, use of white space)

FEEDBACK
I will provide lots of feedback on all designs submitted so that together we can get the best result.

For clarification this is a DESIGN ONLY project. Our website developer will view the designs before we make our final choice as he wants to ensure he can develop "sharp, practical and most importantly light weight web interface" from the design.

Just updated this brief to clarify design issues, content issues and to give some more examples of site designs I like. 

Please note that although we wish to keep the logo you can change the colours to suit your design. 

Please note that we have now added details of pictures we would be happy to use on the website.  We would prefer it if you used one of these.   Otherwise please ensure your picture includes a nice dog and nice cat and no people!

I have been delighted with the quality of the designs submitted for this project.  So much so that I am going to extend the project to include some additional inner pages.   The amended brief will be posted on here on Friday 10 May.   The deadline will be extended and the budget will also be increased. 

Reason: Additional inner pages now required. Budget will be increased. Revised brief to be posted on here Friday 10 May.

Target Market(s)

Pet owners in the UK who are confused about pet insurance. It therefore needs to be a bold design which is plain, clean and easy to read. It should use bold colours rather than pastels and should not use "cuddly" images.

Industry/Entity Type

Insurance

Requirements
Must have
• Bold clear and distinct colours (preferably 5)
Content as per uploaded file (not just content from existing site)
Easy to read fonts
Should not have
• Pastel colours
Cuddly images

```html
<!DOCTYPE html>
<html lang="en">
<head>
<meta charset="utf-8">
<title>Cover Compare Quizzo UK</title>
<link href="https://fonts.googleapis.com/css2?family=Ubuntu:wght@400;500;700&family=PT+Sans:ital,wght@0,400;0,700;1,400&family=Open+Sans:ital,wght@0,400;0,600;0,700;1,400&display=swap" rel="stylesheet">
<style>
:root{
  --black:#050505;
  --nav:#2b86e0;
  --nav-dark:#1a63b3;
  --blue:#1e90e0;
  --orange:#f7841e;
  --purple:#a25ee6;
  --green:#6cbd70;
  --grey:#7c7c7c;
  --head-blue:#2f7bcf;
  --link-orange:#ef7d22;
  --text:#555;
  --rule:#dcdcdc;
  --footer:#4a4a4a;
  --footer-dark:#333;
  --box-blue:#1f5ea6;
  --box-teal:#22b2d1;
  --box-green:#58a96a;
}
*{box-sizing:border-box;margin:0;padding:0}
html,body{width:686px;height:1200px;overflow:hidden}
body{background:#f3f3f3;font-family:"Open Sans",sans-serif;color:var(--text);position:relative}
.abs{position:absolute}
.header{left:0;top:0;width:686px;height:56px;background:var(--black)}
.brand{left:92px;top:12px;display:flex;align-items:center;gap:6px}
.brand-mark{width:24px;height:24px;border-radius:50%;background:#2c7fd6}
.brand-name{font-family:"Ubuntu",sans-serif;font-weight:500;color:#fff;font-size:14px;line-height:14px;width:110px}
.search{left:474px;top:19px;width:126px;height:19px;background:#fff;border-radius:2px}
.search svg{position:absolute;right:4px;top:2px}
.page{left:69px;top:56px;width:548px;height:914px;background:#fff;border-left:1px solid #e2e2e2;border-right:1px solid #e2e2e2}
.nav{left:62px;top:58px;width:561px;height:26px;background:linear-gradient(#3b94ea,var(--nav));box-shadow:0 2px 3px rgba(0,0,0,.25)}
.nav-fold{top:84px;width:0;height:0;border-top:8px solid var(--nav-dark)}
.nav ul{list-style:none;position:relative;height:100%}
.nav li{position:absolute;top:7px;transform:translateX(-50%);color:#fff;font-family:"Ubuntu",sans-serif;font-size:8.5px;white-space:nowrap}
.hero{left:77px;top:84px;width:532px;height:210px;background:linear-gradient(90deg,#e9e6e0,#c9b79c 40%,#8a6e4e 60%,#eeeeee);border:1px solid #ddd}
.hero-caption{left:77px;top:259px;width:532px;height:35px;background:rgba(110,110,110,.75)}
.hero-caption p{position:absolute;left:10px;top:7px;font-family:"PT Sans",sans-serif;font-style:italic;color:#fff;font-size:14.5px}
.dots{position:absolute;right:16px;top:14px;display:flex;gap:3px}
.dots i{width:7px;height:7px;border-radius:50%;background:#444}
.dots i:first-child{background:#2a86e0}
.lookup{left:425px;top:114px;width:171px;height:124px;background:linear-gradient(#fb9a3a,var(--orange));border-radius:4px;box-shadow:0 3px 5px rgba(0,0,0,.25)}
.lookup h2{position:absolute;left:30px;top:8px;font-family:"Ubuntu",sans-serif;font-weight:400;color:#fff;font-size:13px}
.lookup .lens{position:absolute;left:11px;top:11px}
.select{position:absolute;left:11px;width:147px;height:18px;background:#fff;border-radius:2px;font-size:7px;font-style:italic;color:#666;padding:4px 0 0 7px}
.select:after{content:"";position:absolute;right:6px;top:8px;border:4px solid transparent;border-top:3px solid #555}
.lookup .btn{position:absolute;right:13px;top:96px;width:48px;height:17px;background:#222;color:#fff;font-size:7.5px;text-align:center;line-height:17px;border-radius:3px}
.tile{top:310px;width:98px;height:74px;border-radius:3px;padding:7px 9px;color:#fff}
.tile h3{font-family:"PT Sans",sans-serif;font-size:10.5px;line-height:11px;margin-bottom:4px}
.tile p{font-size:6.4px;line-height:10px;opacity:.9}
.t-blue{background:var(--blue)}.t-orange{background:var(--orange)}.t-purple{background:var(--purple)}.t-green{background:var(--green)}.t-grey{background:var(--grey)}
.h-blue{font-family:"PT Sans",sans-serif;font-weight:400;color:var(--head-blue);font-size:12.5px}
.body-text{font-size:6.5px;line-height:11.4px;color:#555}
.more{font-size:6.3px;font-weight:700;color:var(--link-orange)}
.rule{height:1px;background:var(--rule)}
.photo{background:linear-gradient(135deg,#c9a77c,#8d7761 50%,#dfd2bf)}
.ad{left:454px;top:398px;width:143px;height:143px;background:#fff;border:1px solid #c9c9c9}
.ad-top{position:absolute;left:0;top:0;width:141px;height:28px;background:linear-gradient(#78b83a,#5d9d2a)}
.ad-top span{position:absolute;left:3px;top:14px;color:#fff;font-family:"PT Sans",sans-serif;font-size:8px;font-weight:700}
.ad-brand{position:absolute;left:9px;top:46px;font-size:7px;font-weight:700;color:#3b6b1e}
.ad-photo{position:absolute;left:0;top:62px;width:72px;height:79px;background:linear-gradient(#f0d8b4,#cfa57c)}
.ad ul{position:absolute;left:74px;top:46px;list-style:none;font-size:5.4px;line-height:6.2px;color:#333;font-weight:600}
.ad li{margin-bottom:3px}
.ad li.red{color:#d42020}
.ad-cta{position:absolute;left:72px;top:120px;width:64px;height:16px;border-radius:8px;background:#c3141b;color:#fff;font-size:7px;font-style:italic;text-align:center;line-height:16px}
.side{left:439px;top:550px;width:173px;height:212px;background:#f7f7f7;border:1px solid #e3e3e3;border-radius:3px}
.tweet{position:absolute;left:13px;width:150px}
.tweet .thumb{position:absolute;left:0;top:0;width:32px;height:28px}
.tweet p{position:absolute;left:39px;top:-3px;font-size:6.3px;line-height:10px;font-style:italic;color:#555;width:105px}
.tweet .meta{position:absolute;left:39px;top:34px;width:106px;font-size:5.6px;font-style:italic;color:#2f7bcf}
.tweet .meta b{float:right;font-weight:400;color:var(--link-orange)}
.panel{top:775px;width:171px;height:192px;background:#f7f7f7;border:1px solid #e0e0e0;border-radius:3px}
.panel-head{height:22px;color:#fff;font-family:"PT Sans",sans-serif;font-size:10px;padding:4px 8px;position:relative;border-radius:3px 3px 0 0}
.panel-head .arrows{position:absolute;right:7px;top:4px;font-size:10px;letter-spacing:6px}
.entry{position:absolute;left:9px;width:152px;font-size:6.4px;line-height:10.2px;color:#333;font-weight:600}
.entry i{display:block;font-weight:400;color:#2f6fb8;font-size:5.6px}
.entry-rule{position:absolute;left:9px;width:152px;height:1px;background:#ddd}
.readall{position:absolute;right:12px;top:175px;font-size:6.8px;color:#333}
.footer{left:0;top:970px;width:686px;height:170px;background:var(--footer)}
.footbar{left:0;top:1140px;width:686px;height:32px;background:var(--footer-dark)}
.footbar p{text-align:center;font-size:5.8px;color:#bbb;padding-top:11px}
.footbar b{color:#fff;font-weight:400}
.fbox{top:986px;width:171px;height:143px;background:#fff;border-radius:2px}
.fbox-head{height:19px;font-size:7.3px;color:#1f4f86;font-weight:600;padding:5px 0 0 17px;position:relative}
.fbox-head:before{content:"";position:absolute;left:7px;top:5px;width:6px;height:9px;background:currentColor}
.fb-item{position:absolute;left:7px;width:160px}
.fb-item .av{position:absolute;left:0;top:0;width:24px;height:24px;background:linear-gradient(#e7c9a2,#b99170)}
.fb-item h4{position:absolute;left:30px;top:-2px;font-size:7px;color:#2f6fb8;font-weight:600}
.fb-item p{position:absolute;left:30px;top:8px;font-size:5.8px;line-height:8.5px;color:#555;width:125px}
.faces{position:absolute;left:9px;top:134px}
.tw-item{position:absolute;left:10px;width:150px;font-size:6px;line-height:10px;color:#444}
.tw-item a{color:#2f6fb8;text-decoration:none}
.tw-item i{display:block;font-size:5.4px;color:#2f6fb8;margin-top:3px}
.connect{left:471px;top:991px;color:#fff;font-size:7.5px;font-weight:600}
.social{left:471px;display:flex;align-items:center;gap:10px;font-size:6.5px;color:#ddd}
.social i{width:16px;height:16px;border-radius:2px;display:block}
</style>
</head>
<body>
<header class="abs header">
  <div class="abs brand"><span class="brand-mark"></span><span class="brand-name">Cover Compare Quizzo UK</span></div>
  <div class="abs search"><svg width="16" height="14" viewBox="0 0 16 14"><circle cx="6" cy="6" r="4.3" fill="none" stroke="#2c7fd6" stroke-width="2"/><path d="M9 9l5 4" stroke="#2c7fd6" stroke-width="2.4" stroke-linecap="round"/></svg></div>
</header>

<div class="abs page"></div>

<span class="abs nav-fold" style="left:62px;border-left:7px solid transparent"></span>
<span class="abs nav-fold" style="left:616px;border-right:7px solid transparent"></span>
<nav class="abs nav"><ul>
  <li style="left:30px">Home</li><li style="left:96px">Policies »</li><li style="left:165px">Glossary</li>
  <li style="left:240px">Fact Sheets</li><li style="left:328px">Survey Reports</li><li style="left:429px">News &amp; Comment</li><li style="left:522px">Contact Us</li>
</ul></nav>

<div class="abs hero" role="img" aria-label="Photo of a Siamese cat beside a shepherd puppy"></div>
<div class="abs hero-caption"><p>Vestibulum ante ipsum primis in faucibus orci luctus et ultrices......</p><div class="dots"><i></i><i></i><i></i><i></i></div></div>

<section class="abs lookup">
  <svg class="lens" width="16" height="16" viewBox="0 0 16 16"><circle cx="6" cy="6" r="4" fill="none" stroke="#fff" stroke-width="1.8"/><path d="M9 9l5 5" stroke="#fff" stroke-width="2.2" stroke-linecap="round"/></svg>
  <h2>Check Out a Policy</h2>
  <div class="select" style="top:36px">--Select Company --</div>
  <div class="select" style="top:67px">--Select Policy --</div>
  <div class="btn">Search</div>
</section>

<div class="abs tile t-blue" style="left:74px"><h3>Policy Files</h3><p>Full policy details includ-ing type of vet fees cover and limits, ratings, age limits...</p></div>
<div class="abs tile t-orange" style="left:184px"><h3>Policy Search</h3><p>Exclusive to CCQ friends. Search our database of more than 200 policies.</p></div>
<div class="abs tile t-purple" style="left:294px"><h3>Fact Sheets</h3><p>Learn about pet insur-ance. A little knowledge is essential to choosing the right policy..</p></div>
<div class="abs tile t-green" style="left:404px"><h3>Policy Listings by Type</h3><p>Full lists of continuous policies (aka "lifetime policies)...</p></div>
<div class="abs tile t-grey" style="left:513px"><h3>Claims Survey</h3><p>Made a claim in the last 12 months? Please help us to help others by completing....</p></div>

<h2 class="abs h-blue" style="left:75px;top:395px">Welcome to Cover Compare Quizzo UK</h2>
<p class="abs body-text" style="left:75px;top:414px;width:340px">This is an independent website dedicated to helping you to find the best pet insurance policy for your pet.<br>Here you will find unbiased detailed information about almost all of the 205 pet insurance policies currently available in the UK (we hope the other 3 will follow shortly!)<br>We do NOT sell any pet insurance policies nor do we receive commission from any insurance companies.</p>
<div class="abs rule" style="left:74px;top:498px;width:355px"></div>

<aside class="abs ad">
  <div class="ad-top"><span>Term Life Insurance in Minutes</span></div>
  <div class="ad-brand">Steadyleaf Policy</div>
  <div class="ad-photo" role="img" aria-label="Photo of a mother and daughter smiling"></div>
  <ul><li>• Instant Coverage-<br>If Qualified</li><li class="red">• NO MEDICAL EXAM<br><span style="color:#333">Just a few health questions</span></li><li>• 3 Easy-Step Process</li></ul>
  <div class="ad-cta">Free Quote!</div>
</aside>

<h2 class="abs h-blue" style="left:75px;top:510px">About Cover Compare Quizzo UK</h2>
<div class="abs photo" style="left:74px;top:538px;width:100px;height:74px" role="img" aria-label="Photo of children hugging a dog"></div>
<p class="abs body-text" style="left:186px;top:536px;width:242px">Our mission is quite simple - to help you make the right choice about pet insurance for your pet.<br>We are independent and aim to be totally unbiased.<br>We aim to give you as much information about policies, premiums and the experiences of other pet owners as possible.</p>
<span class="abs more" style="left:186px;top:602px">READ MORE</span>
<div class="abs rule" style="left:74px;top:626px;width:355px"></div>

<h2 class="abs" style="left:75px;top:636px;font-family:'PT Sans',sans-serif;font-weight:400;color:#333;font-size:11px">News and Comment</h2>
<div class="abs" style="left:74px;top:660px;width:110px"><h3 class="h-blue" style="font-size:8.5px">Coming soon...</h3><p class="body-text" style="margin-top:2px">It has taken almost a year to get CCQ launched and there is so much more we want to do. Our plans for the year ahead include..</p><p class="more" style="margin-top:4px">READ MORE</p></div>
<div class="abs" style="left:199px;top:660px;width:110px"><h3 class="h-blue" style="font-size:8.5px">Coming soon...</h3><p class="body-text" style="margin-top:2px">It has taken almost a year to get CCQ launched and there is so much more we want to do. Our plans for the year ahead include..</p><p class="more" style="margin-top:4px">READ MORE</p></div>
<div class="abs" style="left:324px;top:660px;width:110px"><h3 class="h-blue" style="font-size:8.5px">Coming soon...</h3><p class="body-text" style="margin-top:2px">It has taken almost a year to get CCQ launched and there is so much more we want to do. Our plans for the year ahead include..</p><p class="more" style="margin-top:4px">READ MORE</p></div>

<aside class="abs side">
  <h2 class="h-blue" style="position:absolute;left:13px;top:8px;font-size:11.5px">Charity Tweets</h2>
  <div class="rule" style="position:absolute;left:13px;top:27px;width:150px"></div>
  <div class="tweet" style="top:32px"><div class="thumb photo" role="img" aria-label="Photo of a dog"></div><p>Aenean lacinia sodales eros, sit amet molestie enim consectetur eget....</p><div class="meta">Read More<b>On 30Apr, 2013</b></div></div>
  <div class="rule" style="position:absolute;left:13px;top:80px;width:150px"></div>
  <div class="tweet" style="top:85px"><div class="thumb photo" role="img" aria-label="Photo of a vet with a pet"></div><p>Aenean lacinia sodales eros, sit amet molestie enim consectetur eget....</p><div class="meta">Read More<b>On 30Apr, 2013</b></div></div>
  <div class="rule" style="position:absolute;left:13px;top:133px;width:150px"></div>
  <div class="tweet" style="top:139px"><div class="thumb photo" role="img" aria-label="Photo of a golden dog"></div><p>Aenean lacinia sodales eros, sit amet molestie enim consectetur eget....</p><div class="meta">Read More<b>On 30Apr, 2013</b></div></div>
  <div class="rule" style="position:absolute;left:13px;top:187px;width:150px"></div>
  <span style="position:absolute;left:14px;top:193px;font-size:6.8px;color:#333">READ ALL&gt;&gt;</span>
</aside>

<section class="abs panel" style="left:74px">
  <div class="panel-head" style="background:var(--box-blue)">Popular Fact Sheets<span class="arrows">‹›</span></div>
  <div class="entry" style="top:30px">Vestibulum ante ipsum primis in faucibus orci luctus et ultrices posuere cubilia.....<i>Posted on Apr19, 2013</i></div>
  <div class="entry-rule" style="top:66px"></div>
  <div class="entry" style="top:76px">Vestibulum ante ipsum primis in faucibus orci luctus et ultrices posuere cubilia.....<i>Posted on Apr19, 2013</i></div>
  <div class="entry-rule" style="top:112px"></div>
  <div class="entry" style="top:122px">Vestibulum ante ipsum primis in faucibus orci luctus et ultrices posuere cubilia.....<i>Posted on Apr19, 2013</i></div>
  <span class="readall">READ ALL &gt;&gt;</span>
</section>
<section class="abs panel" style="left:257px">
  <div class="panel-head" style="background:var(--box-teal)">Recent Reviews<span class="arrows">‹›</span></div>
  <div class="entry" style="top:30px">Vestibulum ante ipsum primis in faucibus orci luctus et ultrices posuere cubilia.....<i>Posted on Apr19, 2013</i></div>
  <div class="entry-rule" style="top:66px"></div>
  <div class="entry" style="top:76px">Vestibulum ante ipsum primis in faucibus orci luctus et ultrices posuere cubilia.....<i>Posted on Apr19, 2013</i></div>
  <div class="entry-rule" style="top:112px"></div>
  <div class="entry" style="top:122px">Vestibulum ante ipsum primis in faucibus orci luctus et ultrices posuere cubilia.....<i>Posted on Apr19, 2013</i></div>
  <span class="readall">READ ALL &gt;&gt;</span>
</section>
<section class="abs panel" style="left:440px">
  <div class="panel-head" style="background:var(--box-green)">Recommended Articles<span class="arrows">‹›</span></div>
  <div class="entry" style="top:30px">Vestibulum ante ipsum primis in faucibus orci luctus et ultrices posuere cubilia.....<i>Posted on Apr19, 2013</i></div>
  <div class="entry-rule" style="top:66px"></div>
  <div class="entry" style="top:76px">Vestibulum ante ipsum primis in faucibus orci luctus et ultrices posuere cubilia.....<i>Posted on Apr19, 2013</i></div>
  <div class="entry-rule" style="top:112px"></div>
  <div class="entry" style="top:122px">Vestibulum ante ipsum primis in faucibus orci luctus et ultrices posuere cubilia.....<i>Posted on Apr19, 2013</i></div>
  <span class="readall">READ ALL&gt;&gt;</span>
</section>

<footer class="abs footer"></footer>
<section class="abs fbox" style="left:74px">
  <div class="fbox-head" style="background:#dde9f5">FRIENDWALL FEEDS</div>
  <div class="fb-item" style="top:26px"><div class="av" role="img" aria-label="Profile photo"></div><h4>Lorem ipsum dolor</h4><p>Duis aliquam nibh a dui iaculis viverra id a velit.</p></div>
  <div class="fb-item" style="top:61px"><div class="av" role="img" aria-label="Profile photo"></div><h4>Lorem ipsum dolor</h4><p>Duis aliquam nibh a dui iaculis viverra id a velit.</p></div>
  <p style="position:absolute;left:8px;top:93px;font-size:5px;color:#333">You and 14,596 others like <b style="color:#2f6fb8">Cover Compare Quizzo UK</b></p>
  <svg class="faces" width="155" height="0"></svg>
  <div style="position:absolute;left:9px;top:101px;display:flex;gap:2px">
    <span style="width:23px;height:23px;background:#b9a58d" role="img" aria-label="Follower photo"></span>
    <span style="width:23px;height:23px;background:#d8dde4"></span>
    <span style="width:23px;height:23px;background:#9a9a8a" role="img" aria-label="Follower photo"></span>
    <span style="width:23px;height:23px;background:#6e6e6e" role="img" aria-label="Follower photo"></span>
    <span style="width:23px;height:23px;background:#c4a287" role="img" aria-label="Follower photo"></span>
    <span style="width:23px;height:23px;background:#e4e8d8"></span>
  </div>
  <p style="position:absolute;left:9px;top:131px;font-size:4.5px;color:#666">Friendwall social plugin</p>
</section>
<section class="abs fbox" style="left:258px">
  <div class="fbox-head" style="background:#7dd0e8;color:#1b4f7a">CHIRPLINE FEEDS</div>
  <div class="tw-item" style="top:26px">Vestibulum<a>http://gdjgg@kulkuf</a> aucibus orci luctus et ultrices posuere cubilia.....<i>3 hrs ago | Re -Tweet</i></div>
  <div style="position:absolute;left:10px;top:72px;width:150px;height:1px;background:#ddd"></div>
  <div class="tw-item" style="top:76px">Vestibulum<a>http://gdjgg@kulkuf</a> aucibus orci luctus et ultrices posuere cubilia.....<i>3 hrs ago | Re -Tweet</i></div>
  <span style="position:absolute;left:11px;top:124px;font-size:6.8px;color:#333">READ ALL &gt;&gt;</span>
</section>
<h3 class="abs connect">CONNECT US</h3>
<div class="abs social" style="top:1010px"><i style="background:#3b5b9a"></i>Friendwall</div>
<div class="abs social" style="top:1035px"><i style="background:#5ab7e0"></i>Chirpline</div>
<div class="abs social" style="top:1060px"><i style="background:#c4302b"></i>Clipstream</div>
<div class="abs social" style="top:1085px"><i style="background:#f0851f"></i>Rss Feed</div>
<div class="abs footbar"><p>Copyright ©2013. <b>Cover-Compare-Quizzo UK.</b> All Right Reserved</p></div>
</body>
</html>
```